Talented energy healer needs business card design

I need a business card design for a new energy healing business in Perth Australia. As an energy healer I am quite earthy and practical rather than floaty and fairydust.
One of the techniques I use is unique in Australia but used internationally (US, UK and Europe). I practice with Coastal Pathway Therapy, Reiki and massage as well as some other techniques I developed personally. I am starting to incorporate sound healing into my practice. I literally change people's lives. The potential for each client is wide open. A key skill I bring to my practice is the capacity for making difficult situations seem more fun and less stressful.
Clients are likely to be depressed, physically unwell, going through a difficult time, unhappy with their current situation. They are people looking for new options to solve a difficult existing problem. They have probably tried other avenues before they come to me. They are open to something different.

I would like to communicate that the client and I work together for their healing and personal growth. I would like to convey that while the work of changing is challenging it can also be fun.

Hi all, info required on the card is:

Name
Title: Healer
contact number (mobile)
I don''t have a logo - I would be interested in seeing designs that use the whole card as well as the traditional logo on one side / in one corner. Whatever ''look/feel'' I choose will carry over to the website as well.

thanks
Meg

Reason: One or two of the designs caught my eye and many appeal for different reasons, but nothing is quite right for me. I've invited a couple of other designers to contribute so I wanted to give them time to be involved. kind regards Meg

Thank you all for the fabulous designs. I really appreciated the thought that many people put into my brief and a number of designs captured important things about what I was trying to say. It was a hard choice between 3 designs in the end.
thanks again and kind regards
Meg

Target Market(s)

people looking for new options to solve a difficult existing problem

Industry/Entity Type

Massage

Logo styles of interest
Abstract Logo
Requirements
Must have
• include green and blue
Nice to have
• hands, tea / teapots , the ocean, stepping stones

```html
<!DOCTYPE html>
<html lang="en">
<head>
<meta charset="utf-8">
<title>Meg Healer – Business Card</title>
<link rel="stylesheet" href="https://fonts.googleapis.com/css2?family=Libre+Baskerville:wght@700&family=Open+Sans:wght@600&display=swap">
<style>
  :root {
    --backdrop: #ece9e4;
    --card-edge: #8a8a8a;
    --name-green: #1f6e36;
    --ink-dark: #111111;
    --ink-service: #2e2e2e;
    --outline-white: #ffffff;
    --sky: #9ec6ea;
    --flame: #d99a62;
    --meadow: #7fae5c;
    --sea: #5b88b4;
  }
  * { box-sizing: border-box; margin: 0; padding: 0; }
  html, body {
    width: 1200px;
    height: 399px;
    overflow: hidden;
    background: var(--backdrop);
  }
  .canvas {
    position: relative;
    width: 1200px;
    height: 399px;
  }
  .card {
    position: absolute;
    top: 43px;
    width: 526px;
    height: 300px;
    border: 1px solid var(--card-edge);
    overflow: hidden;
  }
  .card--front { left: 45px; }
  .card--back { left: 614px; }

  .elements-artwork {
    position: absolute;
    inset: 0;
    background: linear-gradient(135deg, var(--sky) 0%, #c9d7e2 30%, var(--flame) 48%, var(--meadow) 56%, var(--sea) 100%);
  }
  .elements-artwork--faded { opacity: 0.22; }

  .brand-name {
    position: absolute;
    left: 52px;
    top: 18px;
    font-family: "Libre Baskerville", Georgia, serif;
    font-weight: 700;
    font-size: 60px;
    line-height: 1;
    color: var(--name-green);
    -webkit-text-stroke: 1.5px var(--outline-white);
    paint-order: stroke fill;
  }
  .brand-title {
    position: absolute;
    left: 55px;
    top: 76px;
    font-family: "Libre Baskerville", Georgia, serif;
    font-weight: 700;
    font-size: 31px;
    letter-spacing: 2px;
    line-height: 1;
    color: var(--name-green);
    -webkit-text-stroke: 1.5px var(--outline-white);
    paint-order: stroke fill;
  }
  .contact-call,
  .contact-phone {
    position: absolute;
    right: 0;
    font-family: "Open Sans", Arial, sans-serif;
    font-weight: 600;
    color: var(--ink-dark);
    -webkit-text-stroke: 3px var(--outline-white);
    paint-order: stroke fill;
    line-height: 1;
  }
  .contact-call {
    right: 80px;
    top: 30px;
    font-size: 44px;
  }
  .contact-phone {
    right: 6px;
    top: 80px;
    font-size: 28px;
    letter-spacing: 1px;
  }

  .service-list {
    position: absolute;
    inset: 0;
    list-style: none;
    font-family: "Libre Baskerville", Georgia, serif;
    font-weight: 700;
    font-size: 20px;
    color: var(--ink-service);
    text-align: center;
  }
  .service-list li {
    position: absolute;
    left: 0;
    right: 0;
    line-height: 1;
  }
  .service-list li::before { content: "· "; }
  .service-list li:nth-child(1) { top: 76px; }
  .service-list li:nth-child(2) { top: 127px; }
  .service-list li:nth-child(3) { top: 178px; }
  .service-list li:nth-child(4) { top: 229px; }
</style>
</head>
<body>
  <main class="canvas">
    <section class="card card--front">
      <div class="elements-artwork" role="img" aria-label="Photo collage of sky, fire, grass and ocean water with a meditating figure silhouette inside a glass sphere"></div>
      <h1 class="brand-name">Meg</h1>
      <p class="brand-title">Healer</p>
      <p class="contact-call">Call</p>
      <p class="contact-phone">+618-555-014</p>
    </section>

    <section class="card card--back">
      <div class="elements-artwork elements-artwork--faded" role="img" aria-label="Faded photo collage of sky, fire, grass and ocean water with a meditating figure silhouette"></div>
      <ul class="service-list">
        <li>Coastal Pathway Therapy</li>
        <li>Reiki</li>
        <li>Massage</li>
        <li>Sound Healing</li>
      </ul>
    </section>
  </main>
</body>
</html>
```